Business Card Design Project

for a second hand vintage clothing store. shop name is The Velvet Cupboard

Cards to be double sided

The name on the card is Joanna Whitfield

Information to put on card:

The Velvet Cupboard
Joanna Whitfield (no job title)
42/871 Dunmore St, Glenwick, Marlow Bay, NSW, 2741.
Mobile: 0412 905 261
Email: thevelvetcupboard@mailbox.com.au
Web: www.thevelvetcupboard.com.au

Target Market(s)

Women looking at vintage clothing

Industry/Entity Type

Clothing

```html
<!DOCTYPE html>
<html lang="en">
<head>
<meta charset="utf-8">
<title>The Velvet Cupboard – Business Card</title>
<link rel="stylesheet" href="https://fonts.googleapis.com/css2?family=Courier+Prime&family=Parisienne&family=Signika:wght@400;600&display=swap">
<style>
  :root {
    --paper: #ffffff;
    --magenta: #9e1a5b;
    --plum: #55233a;
    --panel: #552436;
    --orange: #f49a1c;
    --cream: #f3dca2;
    --ink-light: #ffffff;
    --label-ink: #111111;
  }
  * { margin: 0; padding: 0; box-sizing: border-box; }
  html, body { width: 933px; height: 1200px; overflow: hidden; background: var(--paper); }
  .sheet { position: relative; width: 933px; height: 1200px; }

  .sheet-label {
    position: absolute; left: 0; width: 100%;
    text-align: center;
    font-family: "Courier Prime", monospace;
    font-size: 28px; color: var(--label-ink);
    letter-spacing: 1px;
  }
  .sheet-label--front { top: 22px; }
  .sheet-label--back { top: 628px; }

  .card { position: absolute; left: 0; width: 933px; height: 536px; background: var(--magenta); overflow: hidden; }
  .card--front { top: 65px; }
  .card--back { top: 664px; }

  /* Front */
  .frame-ornament {
    position: absolute; left: 75px; top: 19px; width: 787px; height: 498px;
  }
  .front-panel {
    position: absolute; left: 150px; top: 108px; width: 633px; height: 320px;
    background: var(--panel); border: 4px solid var(--orange); border-radius: 28px;
    display: flex; align-items: center; justify-content: center;
  }
  .brand-name {
    font-family: "Signika", sans-serif; font-weight: 600;
    font-size: 60px; color: var(--cream); letter-spacing: 1px;
    white-space: nowrap;
  }

  /* Back */
  .side-band {
    position: absolute; top: 0; width: 84px; height: 536px;
    background: var(--plum);
  }
  .side-band--left { left: 0; border-right: 6px solid var(--orange); }
  .side-band--right { right: 0; border-left: 6px solid var(--orange); }
  .vine-ornament { position: absolute; top: 20px; left: 14px; width: 52px; height: 496px; }

  .contact {
    position: absolute; left: 84px; right: 84px; top: 0;
    text-align: center; color: var(--ink-light);
    font-family: "Signika", sans-serif; font-weight: 400; font-size: 25px; line-height: 37px;
  }
  .contact p { white-space: nowrap; }
  .contact__person {
    font-family: "Parisienne", cursive; font-size: 58px; line-height: 1;
    margin-top: 88px; margin-bottom: 40px; font-weight: 400;
  }
  .contact__company { font-weight: 600; }
  .contact__gap { height: 30px; }
</style>
</head>
<body>
<main class="sheet">
  <p class="sheet-label sheet-label--front">Business Card Front Design</p>

  <section class="card card--front" aria-label="Card front">
    <svg class="frame-ornament" viewBox="0 0 787 498" role="img" aria-label="Ornate orange and cream scrolled frame surrounding the shop name">
      <defs>
        <linearGradient id="frameTone" x1="0" y1="0" x2="0" y2="1">
          <stop offset="0" stop-color="#f49a1c"/>
          <stop offset="0.5" stop-color="#e9b45a"/>
          <stop offset="1" stop-color="#f49a1c"/>
        </linearGradient>
      </defs>
      <rect x="0" y="0" width="787" height="498" rx="60" fill="url(#frameTone)"/>
    </svg>
    <div class="front-panel">
      <h1 class="brand-name">The Velvet Cupboard</h1>
    </div>
  </section>

  <p class="sheet-label sheet-label--back">Business Card Back Design</p>

  <section class="card card--back" aria-label="Card back">
    <div class="side-band side-band--left">
      <svg class="vine-ornament" viewBox="0 0 52 496" role="img" aria-label="Orange scrolling vine ornament">
        <rect width="52" height="496" rx="20" fill="#c46a2a" opacity="0.55"/>
      </svg>
    </div>
    <div class="side-band side-band--right">
      <svg class="vine-ornament" viewBox="0 0 52 496" role="img" aria-label="Orange scrolling vine ornament">
        <rect width="52" height="496" rx="20" fill="#c46a2a" opacity="0.55"/>
      </svg>
    </div>

    <div class="contact">
      <h2 class="contact__person">Joanna Whitfield</h2>
      <p class="contact__company">The Velvet Cupboard</p>
      <p>42/871 Dunmore St, Glenwick</p>
      <p>Marlow Bay, NSW, 2741</p>
      <div class="contact__gap"></div>
      <p>Mob: 0412 905 261</p>
      <p>Email: thevelvetcupboard@mailbox.com.au</p>
      <p>www.thevelvetcupboard.com.au</p>
    </div>
  </section>
</main>
</body>
</html>
```